Gordon Pellbrook Consulting - Web Design Project

We need a web design for my new edgy consulting business specializing in innovation, technology and strategy.

It is our personal goal to turn each client into raving fans by helping them achieve their own business goals and aspirations through assisting them in raising their own innovation and marketing standards.

We provide our personalised and state-of-the-art services to our clients and boards who represent some of the world greatest innovative thinkers.
Updates

Here is some other information which may help shape your thinking.

I've had direct Involvement in the development of the following iPad, iPhone Applications and websites

FarbeyondOzlands.com (TerraLink platform) by Voyage Bureau
http://farbeyondozlands.example.au

Sail Verve by Bright Voyaging
https://apps.example-store.com/au/app/sail-verve/id100000001

uRedlandTR by Travel Territory Board
https://apps.example-store.com/au/app/uredlandtr/id100000002

Wexmoor Trips
http://www.wexmoortrips.example.au

Trek Mapper by Voyage Bureau
http://apps.example-store.com/au/app/trek-mapper/id100000003

Sunward by Sunward Travel Office
https://apps.example-store.com/au/app/sunward/id100000004

Upper Fernridge Valley Route by Visit Coastlands
https://apps.example-store.com/au/app/upper-fernridge-valley-route/id100000005

Wanderer Path by Travel Territory Board and Southern Plains Travel Council
https://apps.example-store.com/au/app/wanderers-path-grand-journey/id100000006

Gordon Pellbrook Consulting (GPC)
November 2012 – Present (8 months)Brisbane, Sydney, Canberra

Gordon’s consults to Small-to-Medium Enterprises (SME) and Government organisations on business strategy, technology strategy, risk mitigation, disruptive technology and innovation in the workplace.

Gordon’s consultancy mantra is that we cannot divorce economic life from cultural life particularly in an era when social capital may be as important as physical capital in business.

Reason: request from designers, I want to see their best efforts

Target Market(s)

35+

Industry/Entity Type

Business

Requirements
Must have
• Please use some of the personal image(s) contained in the zip files which can be downloaded from here

http://filedrop.example/k9Xq2Lm
http://filedrop.example/p4Rt7Vn
http://filedrop.example/z8Hw3Bc
Nice to have
• Black, Sleek design, maybe minimalist. Nice to have a Pixelle for the design. Nice to have it easily ported to Wordpress or be a modified Wordpress template. HTML 5, responsive design

```html
<!DOCTYPE html>
<html lang="en">
<head>
<meta charset="utf-8">
<title>Gordon Pellbrook Consulting</title>
<link rel="stylesheet" href="https://fonts.googleapis.com/css2?family=Oswald:wght@300;400;700&display=swap">
<style>
  :root {
    --sky-top: #b9b6c4;
    --sky-mid: #8a8498;
    --city-dark: #4a4258;
    --city-deep: #2f2a3a;
    --text-light: #ffffff;
    --button: #2c8fd0;
    --button-dark: #1f78b4;
  }
  html, body {
    margin: 0;
    padding: 0;
    width: 1200px;
    height: 722px;
    overflow: hidden;
  }
  .hero {
    position: relative;
    width: 1200px;
    height: 722px;
    overflow: hidden;
    font-family: "Oswald", "Arial Narrow", sans-serif;
    color: var(--text-light);
    text-align: center;
  }
  .hero__backdrop {
    position: absolute;
    inset: 0;
    background:
      radial-gradient(ellipse 70% 35% at 25% 12%, rgba(225,222,232,0.75), transparent 70%),
      radial-gradient(ellipse 60% 50% at 70% 75%, rgba(60,52,74,0.55), transparent 70%),
      linear-gradient(180deg, var(--sky-top) 0%, var(--sky-mid) 30%, var(--city-dark) 65%, var(--city-deep) 100%);
  }
  .hero__backdrop::after {
    content: "";
    position: absolute;
    inset: 0;
    background: rgba(30, 24, 40, 0.18);
  }
  .hero__content {
    position: relative;
    z-index: 1;
  }
  .hero__title {
    margin: 0;
    position: absolute;
    top: 142px;
    left: 0;
    right: 0;
    font-weight: 400;
    font-size: 60px;
    line-height: 1.2;
    color: var(--text-light);
  }
  .hero__mantra {
    margin: 0;
    position: absolute;
    top: 250px;
    left: 0;
    right: 0;
    font-weight: 300;
    font-size: 36px;
    line-height: 56px;
    text-shadow: 0 2px 6px rgba(0,0,0,0.25);
  }
  .hero__cta {
    position: absolute;
    top: 480px;
    left: 50%;
    transform: translateX(-50%);
    display: inline-flex;
    align-items: center;
    gap: 14px;
    padding: 0 20px;
    height: 62px;
    background: var(--button);
    border-bottom: 3px solid var(--button-dark);
    border-radius: 4px;
    font-size: 30px;
    font-weight: 400;
    color: var(--text-light);
    text-decoration: none;
    text-transform: uppercase;
    box-sizing: border-box;
    white-space: nowrap;
  }
  .hero__cta strong {
    font-weight: 700;
  }
  .hero__cta svg {
    width: 14px;
    height: 24px;
  }
</style>
</head>
<body>
  <section class="hero">
    <div class="hero__backdrop" role="img" aria-label="Blurred aerial photograph of a city skyline at dusk"></div>
    <div class="hero__content">
      <h1 class="hero__title">Gordon Pellbrook Consulting</h1>
      <p class="hero__mantra">We cannot divorce economic life from cultural life<br>particularly in an era when social capital may be as important<br>as physical capital in business.</p>
      <a class="hero__cta" href="#services">Get <strong>Innovative</strong>
        <svg viewBox="0 0 14 24" aria-hidden="true"><polyline points="2,2 12,12 2,22" fill="none" stroke="#ffffff" stroke-width="3"/></svg>
      </a>
    </div>
  </section>
</body>
</html>
```